International Development Cooperation Consultant needs a business card design

I need a business card design for myself as a way to present and introduce to wide range of organisations: international organisations, NGOs, governments, universities....
I am a consultant working in the field of governance, civil society and public sector. I carry out studies and provide advice for development agencies as well as think tanks on different topics such as civil society organisations in developing countries, corruption, climate change, monitoring and evaluation. I also provide technical assistance to governments in developing countries... These studies should help for example NGOs to play a better role in poor countries or where they are threatened, or improved the impact of aid in developing countries. Technical capacity should strengthen the organisation and empower the public civl servants in those countries. I would like to see designs that give a fresh, young, positive, alternative but at the same time serious impression. That reflects change, connecting people, the world, knowledge, multi-culturality... Most of people I have worked with say that 'I make things happen' !
Industry/Entity Type
Business
Contact Information for Business Card
Laia Bertran Soler
International Development Consultant
Governance Expert
E-mail: laiabertran@correuweb.example
Phone: +34628351470

```html
<!DOCTYPE html>
<html lang="en">
<head>
<meta charset="UTF-8">
<title>Laia Bertran Soler – Business Card</title>
<link href="https://fonts.googleapis.com/css2?family=Lato:wght@400;700&display=swap" rel="stylesheet">
<style>
  :root {
    --backdrop: #d6d6d6;
    --card: #f7f7f7;
    --band: #e3e2e2;
    --ink: #4a4a4a;
    --ink-soft: #5c5c5c;
    --icon-fill: #4a4a4a;
    --icon-text: #f7f7f7;
  }
  * { margin: 0; padding: 0; box-sizing: border-box; }
  html, body {
    width: 1200px;
    height: 926px;
    overflow: hidden;
    background: var(--backdrop);
    font-family: "Lato", sans-serif;
  }
  .sheet {
    width: 1200px;
    height: 926px;
    display: flex;
    flex-direction: column;
    align-items: center;
    justify-content: center;
    gap: 40px;
  }
  .card {
    position: relative;
    width: 720px;
    height: 411px;
    background: var(--card);
    box-shadow: 0 2px 10px rgba(0,0,0,0.12);
    color: var(--ink);
  }
  .band {
    position: absolute;
    left: 0;
    right: 0;
    background: var(--band);
  }
  .card-front .band { top: 118px; height: 104px; }
  .card-back .band { top: 112px; height: 108px; }

  .holder-name {
    position: absolute;
    left: 44px;
    top: 14px;
    font-weight: 700;
    font-size: 20px;
    letter-spacing: 0.2px;
    text-transform: uppercase;
    color: var(--ink-soft);
  }
  .specialty {
    position: absolute;
    right: 44px;
    bottom: 14px;
    font-size: 19px;
    color: var(--ink-soft);
  }
  .band-phone {
    position: absolute;
    right: 44px;
    bottom: 16px;
    font-size: 17px;
    letter-spacing: 0.5px;
    color: var(--ink-soft);
  }
  .role-title {
    position: absolute;
    left: 44px;
    top: 246px;
    font-size: 24px;
    letter-spacing: 3.2px;
    text-transform: uppercase;
    color: var(--ink);
  }
  .contact-line {
    position: absolute;
    left: 58px;
    top: 294px;
    display: flex;
    align-items: center;
    gap: 12px;
    font-size: 17px;
    letter-spacing: 0.5px;
    color: var(--ink-soft);
  }
  .contact-item { display: flex; align-items: center; gap: 7px; }
  .contact-icon { width: 22px; height: 22px; display: block; }
  .divider { color: var(--ink-soft); padding: 0 8px; }
</style>
</head>
<body>
<main class="sheet">
  <section class="card card-back" aria-label="Business card, back">
    <div class="band">
      <p class="holder-name">Laia Bertran Soler</p>
      <p class="band-phone">+34 628 351 470</p>
    </div>
  </section>

  <section class="card card-front" aria-label="Business card, front">
    <div class="band">
      <p class="holder-name">Laia Bertran Soler</p>
      <p class="specialty">Governance Expert</p>
    </div>
    <p class="role-title">International Development Consultant</p>
    <div class="contact-line">
      <span class="contact-item">
        <svg class="contact-icon" viewBox="0 0 22 22" aria-hidden="true">
          <circle cx="11" cy="11" r="11" fill="var(--icon-fill)"/>
          <text x="11" y="15.5" text-anchor="middle" font-family="Lato, sans-serif" font-weight="700" font-size="13" fill="var(--icon-text)">E</text>
        </svg>
        laiabertran@correuweb.example
      </span>
      <span class="divider">|</span>
      <span class="contact-item">
        <svg class="contact-icon" viewBox="0 0 22 22" aria-hidden="true">
          <circle cx="11" cy="11" r="11" fill="var(--icon-fill)"/>
          <text x="11" y="15.5" text-anchor="middle" font-family="Lato, sans-serif" font-weight="700" font-size="13" fill="var(--icon-text)">P</text>
        </svg>
        +34 628 351 470
      </span>
    </div>
  </section>
</main>
</body>
</html>
```